Private Optometric Practice Needs new Presentation Folders/Stationary

We recently moved our office and are looking to refresh our presentation folders and stationary. I tend to prefer simple, clean designs. We are a full scope optometric practice provide high quality eyewear, custom contact lenses, along with emergency care and treatment for dry eyes. We communicate with a lot of other doctors and want to exude professionalism. I have attached 2 versions of our logo.

Target Market(s)

Familys

Industry/Entity Type

Eyecare

Font styles to use
Sans Serif

Colors
0054AA
0677BA
7BADD7
CADEEF
E8F1F8

Requirements
Nice to have
• Bifold, areas to put information about practice, welcome letter

```html
<!DOCTYPE html>
<html lang="en">
<head>
<meta charset="utf-8">
<title>Clearvista Eyecare – Stationery Set</title>
<link rel="stylesheet" href="https://fonts.googleapis.com/css2?family=Lato:wght@300;400;700&family=Open+Sans:wght@400;600&family=Playfair+Display+SC:wght@400&display=swap">
<style>
  :root{
    --navy:#0b1a29;
    --navy-deep:#040b16;
    --blue:#38a9e0;
    --blue-pale:#e1f0f9;
    --slate:#3c4446;
    --paper:#ffffff;
    --marble:#ebecec;
    --marble-line:#dcdedf;
    --ink:#4a4f55;
    --ink-soft:#8b9096;
  }
  *{box-sizing:border-box;margin:0;padding:0}
  html,body{width:1200px;height:1200px;overflow:hidden}
  body{position:relative;font-family:"Open Sans",Arial,sans-serif;background:var(--slate)}
  .quadrant{position:absolute;width:600px;height:600px;overflow:hidden}
  .quadrant--cards{left:0;top:0;background:var(--slate)}
  .quadrant--folder{left:600px;top:0;background:var(--slate)}
  .quadrant--envelope{left:0;top:600px;background:var(--slate)}
  .quadrant--letterhead{left:600px;top:600px;background:var(--navy-deep)}
  .quadrant__title{position:absolute;top:20px;left:0;width:100%;text-align:center;
    font-family:"Lato",sans-serif;font-weight:400;font-size:21px;color:#fff;letter-spacing:.3px}
  .abs{position:absolute}

  /* wordmark */
  .wordmark{font-family:"Lato",sans-serif;font-weight:400;text-transform:uppercase;text-align:center;line-height:1.15}
  .wordmark span{display:block}
  .wordmark__dot{display:block;margin:0 auto 5px;border-radius:50%;background:var(--blue)}

  /* business card front */
  .card{position:absolute;width:300px;height:172px;overflow:hidden}
  .card--front{left:150px;top:88px;background:var(--navy)}
  .card--front .edge-left{left:0;top:0;width:7px;height:120px;background:var(--blue)}
  .card--front .edge-right{right:0;bottom:0;width:7px;height:120px;background:var(--blue)}
  .card--front .wordmark{left:0;top:44px;width:100%;color:#fff;font-size:15px;letter-spacing:5px}
  .card--front .site{left:0;bottom:18px;width:100%;text-align:center;color:#fff;font-size:9px;letter-spacing:.4px}
  .card--front .rule{height:1px;background:var(--blue);bottom:24px}

  /* business card back */
  .card--back{left:150px;top:300px;background:var(--marble)}
  .card--back .edge-left{left:0;top:0;width:7px;height:110px;background:var(--blue)}
  .card--back .edge-right{right:0;bottom:0;width:7px;height:90px;background:var(--blue)}
  .name{left:22px;top:16px;font-family:"Lato",sans-serif;line-height:1.1}
  .name__first{display:block;font-weight:300;font-size:13px;color:var(--ink);letter-spacing:1px}
  .name__last{display:block;font-weight:700;font-size:13px;color:var(--blue);letter-spacing:.5px}
  .contact-list{list-style:none;left:22px;top:56px;font-size:8.5px;color:var(--ink);line-height:14px}
  .contact-list li{display:flex;align-items:center;gap:6px}
  .contact-list svg{width:9px;height:9px;flex:none}
  .card--back .address-band{left:0;bottom:12px;width:190px;height:17px;background:var(--blue);
    border-radius:0 9px 9px 0;color:#fff;font-size:7.5px;line-height:17px;padding-left:14px}
  .card--back .wordmark{right:22px;bottom:32px;color:var(--ink-soft);font-size:11px;letter-spacing:3px}

  /* folder */
  .panel{position:absolute;top:92px;width:225px;height:300px;overflow:hidden}
  .panel--back{left:70px;background:var(--navy)}
  .panel--front{left:295px;background:var(--marble)}
  .panel--back .wordmark{left:0;top:80px;width:100%;color:#fff;font-size:17px;letter-spacing:5px}
  .panel--back .arcs{left:0;bottom:22px;width:100px;height:40px;background:linear-gradient(90deg,#122435,#0b1a29)}
  .panel--back .contacts{right:12px;bottom:34px;font-size:5.5px;color:#fff;line-height:8px;list-style:none}
  .panel--back .web-band{left:14px;bottom:10px;width:200px;height:9px;background:var(--blue);border-radius:5px;
    color:#fff;font-size:5px;line-height:9px;text-align:center}
  .panel--front .marble{inset:0;background:linear-gradient(135deg,#f1f2f2,#e4e6e7)}
  .panel--front .arcs{right:10px;bottom:70px;width:60px;height:80px;border-radius:30px 30px 0 0;background:#dfe1e2}
  .panel--front .stripe{left:0;top:10px;width:6px;height:40px;background:var(--blue)}
  .panel--front .wordmark{left:18px;top:14px;color:var(--ink-soft);font-size:9px;letter-spacing:2.5px;text-align:left}
  .headline{left:0;top:118px;width:100%;text-align:center;font-family:"Playfair Display SC",serif;line-height:1.2}
  .headline__top{display:block;font-size:17px;color:#3a3f44}
  .headline__accent{display:block;font-size:17px;color:var(--blue)}
  .pocket{position:absolute;top:392px;width:225px;height:78px;background:var(--blue)}
  .pocket--back{left:70px;border-radius:0 0 18px 0}
  .pocket--front{left:295px;border-radius:0 0 0 18px}
  .pocket-notch{position:absolute;left:280px;top:392px;width:30px;height:78px;background:var(--slate);
    clip-path:polygon(50% 0,100% 100%,0 100%)}

  /* envelope */
  .envelope{position:absolute;left:53px;top:176px;width:493px;height:246px;background:var(--paper);overflow:hidden}
  .tab{position:absolute;background:var(--navy);border-bottom:3px solid var(--blue);border-radius:0 0 14px 14px}
  .envelope .tab{left:12px;top:0;width:69px;height:78px}
  .tab .wordmark{position:absolute;left:0;width:100%;color:#fff}
  .envelope .tab .wordmark{top:22px;font-size:7.5px;letter-spacing:2px}
  .envelope .faint-disc{right:-40px;top:60px;width:200px;height:130px;border-radius:50%;background:var(--blue-pale)}
  .envelope .return{left:18px;top:92px;font-size:8px;color:var(--blue);line-height:11px}
  .web-strip{position:absolute;background:var(--blue);color:#fff;transform:skewX(-18deg)}
  .web-strip span{display:block;transform:skewX(18deg)}
  .envelope .web-strip{left:8px;top:219px;width:134px;height:19px;font-size:8px;line-height:19px;padding-left:14px}

  /* letterhead */
  .letterhead{position:absolute;left:127px;top:76px;width:346px;height:448px;background:var(--paper);overflow:hidden}
  .letterhead .band{left:0;top:11px;width:100%;height:48px;background:var(--blue)}
  .letterhead .tab{left:33px;top:0;width:78px;height:85px}
  .letterhead .tab .wordmark{top:28px;font-size:8px;letter-spacing:2px}
  .letterhead .contacts{left:126px;top:20px;list-style:none;font-size:6.5px;color:#fff;line-height:9px}
  .letterhead .contacts li{display:flex;align-items:center;gap:3px}
  .letterhead .contacts svg{width:6px;height:6px}
  .letterhead .address{left:230px;top:25px;font-size:6.5px;color:#fff;line-height:9px;display:flex;gap:3px}
  .letterhead .address svg{width:6px;height:6px;margin-top:1px}
  .letterhead .faint-disc{left:82px;top:188px;width:182px;height:94px;border-radius:50%;background:var(--blue-pale)}
  .letterhead .web-strip{left:36px;top:427px;width:272px;height:14px;font-size:6.5px;line-height:14px;text-align:center}
</style>
</head>
<body>

<!-- Business cards -->
<section class="quadrant quadrant--cards">
  <h2 class="quadrant__title">BUSINESS CARD DESIGN</h2>

  <div class="card card--front">
    <div class="abs edge-left"></div>
    <div class="abs edge-right"></div>
    <div class="abs wordmark"><i class="wordmark__dot" style="width:18px;height:18px"></i><span>Clearvista</span><span>Eyecare</span></div>
    <div class="abs rule" style="left:20px;width:70px"></div>
    <div class="abs rule" style="right:20px;width:70px"></div>
    <div class="abs site">www.clearvistaeyes.com</div>
  </div>

  <div class="card card--back">
    <div class="abs edge-left"></div>
    <div class="abs edge-right"></div>
    <div class="abs name"><span class="name__first">DANIEL</span><span class="name__last">WHITFORD, O.D.</span></div>
    <ul class="abs contact-list">
      <li><svg viewBox="0 0 10 10"><circle cx="5" cy="5" r="4.4" fill="none" stroke="#38a9e0"/><path d="M3.3 3h1.2l.4 1-.6.5c.3.6.7 1 1.3 1.3l.5-.6 1 .4v1.2c-2.4 0-3.8-1.4-3.8-3.8z" fill="#38a9e0"/></svg>(555) 014-2230</li>
      <li><svg viewBox="0 0 10 10"><circle cx="5" cy="5" r="4.4" fill="none" stroke="#38a9e0"/><rect x="3" y="3" width="4" height="4" fill="#38a9e0"/></svg>(555) 014-2231</li>
      <li><svg viewBox="0 0 10 10"><circle cx="5" cy="5" r="4.4" fill="none" stroke="#38a9e0"/><path d="M2.8 5.2 7.2 3 5.6 7.2 5 5.6z" fill="#38a9e0"/></svg>dan@clearvistaeyes.com</li>
      <li><svg viewBox="0 0 10 10"><circle cx="5" cy="5" r="4.4" fill="none" stroke="#38a9e0"/><path d="M1 5h8M5 1v8" stroke="#38a9e0" stroke-width=".8"/></svg>www.clearvistaeyes.com</li>
    </ul>
    <div class="abs address-band">1840 Lakeview Plaza Suite B, Fairmont, MI 48012</div>
    <div class="abs wordmark"><i class="wordmark__dot" style="width:14px;height:14px"></i><span>Clearvista</span><span>Eyecare</span></div>
  </div>
</section>

<!-- Presentation folder -->
<section class="quadrant quadrant--folder">
  <h2 class="quadrant__title">PRESENTATION FOLDER DESIGN</h2>

  <div class="panel panel--back">
    <div class="abs wordmark"><i class="wordmark__dot" style="width:22px;height:22px"></i><span>Clearvista</span><span>Eyecare</span></div>
    <div class="abs arcs" role="img" aria-label="Fine concentric arc line pattern in navy"></div>
    <ul class="abs contacts">
      <li>(555) 014-2230</li>
      <li>(555) 014-2231</li>
      <li>dan@clearvistaeyes.com</li>
      <li>1840 Lakeview Plaza Suite B,</li>
      <li>Fairmont, MI 48012</li>
    </ul>
    <div class="abs web-band">www.clearvistaeyes.com</div>
  </div>

  <div class="panel panel--front">
    <div class="abs marble" role="img" aria-label="Soft grey marble texture"></div>
    <div class="abs arcs" role="img" aria-label="Concentric arch line pattern in light grey"></div>
    <div class="abs stripe"></div>
    <div class="abs wordmark"><span>Clearvista</span><span>Eyecare</span></div>
    <div class="abs headline"><span class="headline__top">Eyesight is</span><span class="headline__accent">Precious</span></div>
  </div>

  <div class="pocket pocket--back"></div>
  <div class="pocket pocket--front"></div>
  <div class="pocket-notch"></div>
</section>

<!-- Envelope -->
<section class="quadrant quadrant--envelope">
  <h2 class="quadrant__title">ENVELOPE DESIGN</h2>
  <div class="envelope">
    <div class="abs faint-disc"></div>
    <div class="tab"><div class="wordmark"><span>Clearvista</span><span>Eyecare</span></div></div>
    <p class="abs return">1840 Lakeview<br>Plaza Suite B, Fairmont,<br>MI 48012</p>
    <div class="web-strip"><span>www.clearvistaeyes.com</span></div>
  </div>
</section>

<!-- Letterhead -->
<section class="quadrant quadrant--letterhead">
  <h2 class="quadrant__title">LETTERHEAD DESIGN</h2>
  <div class="letterhead">
    <div class="abs band"></div>
    <div class="tab"><div class="wordmark"><span>Clearvista</span><span>Eyecare</span></div></div>
    <ul class="abs contacts">
      <li><svg viewBox="0 0 10 10"><circle cx="5" cy="5" r="4.3" fill="none" stroke="#fff"/></svg>(555) 014-2230</li>
      <li><svg viewBox="0 0 10 10"><circle cx="5" cy="5" r="4.3" fill="none" stroke="#fff"/></svg>(555) 014-2231</li>
      <li><svg viewBox="0 0 10 10"><circle cx="5" cy="5" r="4.3" fill="none" stroke="#fff"/></svg>dan@clearvistaeyes.com</li>
    </ul>
    <div class="abs address"><svg viewBox="0 0 10 10"><circle cx="5" cy="5" r="4.3" fill="none" stroke="#fff"/></svg><span>1840 Lakeview Plaza Suite B,<br>Fairmont, MI 48012</span></div>
    <div class="abs faint-disc"></div>
    <div class="web-strip"><span>www.clearvistaeyes.com</span></div>
  </div>
</section>

</body>
</html>
```